Email to encourage School District Employees to save for retirement using the 457 Retirement

This is an email to encourage School District Employees to save for retirement using the 457 Retirement Plan. Highlights of the plan include no 10% IRS penalty for taking money before age 59 1/2 another highlight is that they can save money on taxes by using the plan to reduce their taxable income. This is why they should use the this plan first, not a 403(b). We are financial advisers helping school employees

Target Market(s)

School Employees, Teachers, Administrators, Secretaries. Planning for retirement and reduce taxes.

Industry/Entity Type

Financial Planning

Colors

Designer to choose colors to be used in the design.

Requirements
Must have
• [TEXT]:
• HARBORLINE SAVINGS
• Are you contributing to a 403(b) retirement account? Here’s why you should consider a HARBORLINE SAVINGS
• •No IRS 10% Penalty
• If you leave your job, you can take distributions at any time, no matter your age without penalty, unlike 403(b) accounts which impose a 10% penalty if under age 59 ½.
• •More Tax-Deferral
• You can contribute to both a 457 and 403(b) plan simultaneously. This means defer and save up to $37,000 annually or $49,000 if age 50+. This is especially appealing to employees who have substantially high income and are trying to reduce taxable income.
• DON’T COMPLETELY RELY ON THAT PENSION TO PROVIDE FOR YOUR RETIREMENT. TAKE YOUR FINANCIAL FUTURE INTO YOUR OWN HANDS WITH A 457
• LEARN MORE CALL TODAY
• 800-555-0193
• [8pt font]:
• Securities offered through Birchmont Harbor Securities, L.P. Member - TRELDA/VOMEX | 4876 Quillon Rd, Ste 500, Marbury, CA 90000 | 800.555.0193 | CA Ins. Lic. #7K31508, #0649213, #7K38260, #0915842
Nice to have
• We would like to see a design that shows a teacher writing on chalkboard "Why you should use a HARBORLINE SAVINGS"
• Please emphasize that there is no 10% penalty and that they can save more and reduce taxes using 457 plan. Please use images and themes related to School/Education, money, and retirement.

```html
<!DOCTYPE html>
<html lang="en">
<head>
<meta charset="utf-8">
<title>Harborline Savings</title>
<link rel="stylesheet" href="https://fonts.googleapis.com/css2?family=Roboto:wght@300&family=PT+Sans:wght@400;700&display=swap">
<style>
  :root {
    --brand-blue: #1c6cbf;
    --hero-blue: #2f7fcb;
    --hero-deep: #1d64b1;
    --hero-light: #7fb0e0;
    --text-grey: #6a6a6a;
    --card-border: #eeeeee;
    --footer-bg: #f4f4f4;
    --footer-muted: #9a9a9a;
    --white: #ffffff;
  }
  * { margin: 0; padding: 0; box-sizing: border-box; }
  html, body { width: 1026px; height: 1200px; overflow: hidden; background: var(--white); }
  body { position: relative; font-family: "PT Sans", Arial, sans-serif; color: var(--text-grey); }

  .site-header { position: absolute; left: 0; top: 0; width: 1026px; height: 101px; }
  .brand-name {
    position: absolute; left: 110px; top: 34px;
    font-family: "PT Sans", Arial, sans-serif; font-weight: 700;
    font-size: 29px; line-height: 36px; color: var(--brand-blue);
  }

  .hero { position: absolute; left: 0; top: 101px; width: 1026px; height: 372px; overflow: hidden; }
  .hero-photo {
    position: absolute; inset: 0;
    background:
      radial-gradient(ellipse 200px 260px at 760px 210px, rgba(200,225,248,0.55), rgba(200,225,248,0) 70%),
      linear-gradient(180deg, var(--hero-light) 0%, var(--hero-blue) 38%, var(--hero-deep) 100%);
  }
  .hero-title {
    position: absolute; left: 104px; top: 136px;
    font-family: "Roboto", Arial, sans-serif; font-weight: 300;
    font-size: 36px; line-height: 51px; color: var(--white);
  }

  .benefit-card {
    position: absolute; top: 499px; width: 405px; height: 287px;
    border: 1px solid var(--card-border); padding: 14px 30px 0 30px;
  }
  .benefit-card.penalty { left: 86px; }
  .benefit-card.deferral { left: 517px; }
  .benefit-title { font-weight: 700; font-size: 23px; line-height: 30px; color: var(--brand-blue); }
  .benefit-text { font-size: 19px; line-height: 32px; margin-top: 2px; }
  .penalty .benefit-text { width: 300px; }
  .deferral .benefit-text { width: 345px; }

  .pension-note {
    position: absolute; left: 83px; top: 814px; width: 820px;
    font-size: 19px; line-height: 32px; text-transform: uppercase;
  }
  .call-to-action {
    position: absolute; left: 83px; top: 910px;
    font-size: 19px; line-height: 32px; color: var(--brand-blue); text-transform: uppercase;
  }
  .legal-note {
    position: absolute; left: 83px; top: 974px; width: 850px;
    font-size: 16.5px; line-height: 29.5px;
  }

  .site-footer { position: absolute; left: 0; top: 1071px; width: 1026px; height: 129px; background: var(--footer-bg); }
  .social-links { position: absolute; left: 392px; top: 27px; display: flex; gap: 31px; }
  .social-dot { width: 36px; height: 36px; border-radius: 50%; background: var(--brand-blue); }
  .footer-line { position: absolute; left: 0; width: 1026px; text-align: center; top: 82px; font-size: 15.5px; line-height: 20px; color: var(--text-grey); }
  .footer-line .muted { color: var(--footer-muted); }
</style>
</head>
<body>
  <header class="site-header">
    <div class="brand-name">HARBORLINE SAVINGS</div>
  </header>

  <section class="hero">
    <div class="hero-photo" role="img" aria-label="Retired couple embracing on a lakeside pier, tinted blue"></div>
    <h1 class="hero-title">Are you contributing<br>to a 403(b) retirement<br>account?</h1>
  </section>

  <article class="benefit-card penalty">
    <h2 class="benefit-title">No IRS 10% Penalty</h2>
    <p class="benefit-text">If you leave your job, you can take distributions at any time, no matter your age without penalty, unlike 403(b) accounts which impose a 10% penalty if under age 59 ½.</p>
  </article>

  <article class="benefit-card deferral">
    <h2 class="benefit-title">More Tax-Deferral</h2>
    <p class="benefit-text">You can contribute to both a 457 and 403(b) plan simultaneously. This means defer and save up to $37,000 annually or $49,000 if age 50+. This is especially appealing to employees who have sub-stantially high income and are trying to reduce taxable income.</p>
  </article>

  <p class="pension-note">Don’t completely rely on that pension to provide for your retirement. Take your financial future into your own hands with a 457</p>

  <p class="call-to-action">Learn more call today - 800-555-0193</p>

  <p class="legal-note">Securities offered through Birchmont Harbor Securities, L.P. Member - TRELDA/VOMEX | 4876 Quillon Rd, Ste 500, Marbury, CA 90000 | 800.555.0193 | CA Ins. Lic. #7K31508, #0649213, #7K38260, #0915842</p>

  <footer class="site-footer">
    <div class="social-links">
      <span class="social-dot"></span>
      <span class="social-dot"></span>
      <span class="social-dot"></span>
    </div>
    <p class="footer-line">Harborline insurance © <span class="muted">copyright 2018 - Unsubscribe here</span></p>
  </footer>
</body>
</html>
```